Platelet Rich Plasma (PRP) Flyer

Hi,

Looking to spruce up our Platelet Rich Plasma Flyer (see power point attachment). I also included previous flyers as examples on the design style we are looking for.

Quorum is our official font of our logo.
Attached is our logo in EPS format.
Please use the current photos in the power point. If you include photos, please make sure the stock image is free.

Files must be under 5MB. JPEG, PNG, PDF, .ai

Thank you,
Dorian

Target Market(s)

Patients

Industry/Entity Type

Healthcare

Font styles to use
Other font styles liked:
• Quorum

Requirements
Must have
• Emphasis on Platelet Rich Plasma Therapy when they pick up the flyer. The price of $199. FSA/HSA Eligible. The different treatment areas. The three addresses. Best of the best logo can be very small, not as important.
Nice to have
• One or two pictures. Less is more
Should not have
• Long paragraphs, multiple sentences.

```html
<!DOCTYPE html>
<html lang="en">
<head>
<meta charset="utf-8">
<title>PRP Therapy Flyer</title>
<link rel="stylesheet" href="https://fonts.googleapis.com/css2?family=Poppins:ital,wght@0,400;0,500;0,600;0,700;0,800;1,700;1,800&family=Yellowtail&display=swap">
<style>
  :root {
    --ink: #333333;
    --teal: #4fc3a1;
    --orange: #f07a3e;
    --white: #ffffff;
    --grey-text: #9a9a9a;
    --light-text: #e6e6e6;
    --paper: #ffffff;
    --dark-text: #2a2a2a;
  }
  * { margin: 0; padding: 0; box-sizing: border-box; }
  html, body { width: 973px; height: 1200px; overflow: hidden; background: var(--ink); }
  .flyer {
    position: relative; width: 973px; height: 1200px; overflow: hidden;
    background: var(--ink); font-family: "Poppins", sans-serif; color: var(--white);
  }
  .abs { position: absolute; }
  .brand { left: 57px; top: 62px; display: flex; align-items: center; gap: 12px; }
  .brand-dot { width: 34px; height: 34px; border-radius: 50%; background: var(--teal); }
  .brand-name { font-weight: 700; font-size: 25px; line-height: 1.1; color: var(--orange); letter-spacing: .5px; }
  .script { left: 38px; top: 178px; font-family: "Yellowtail", cursive; font-size: 84px; color: var(--orange); transform: rotate(-4deg); line-height: 1; }
  .headline { left: 53px; font-weight: 800; color: var(--teal); line-height: 1; letter-spacing: -1px; }
  .headline.plasma { top: 262px; font-size: 86px; }
  .headline.therapy { top: 343px; font-size: 86px; }
  .abbr { left: 57px; top: 425px; font-size: 58px; font-weight: 500; color: var(--light-text); line-height: 1; }
  .price-tab { left: 57px; top: 521px; width: 262px; height: 39px; background: var(--orange);
    clip-path: polygon(0 0, 90% 0, 100% 100%, 0 100%); font-size: 28px; font-weight: 500; padding-left: 14px; line-height: 39px; }
  .price-box { left: 57px; top: 559px; width: 398px; height: 111px; border: 2px solid var(--teal); border-radius: 0 10px 10px 10px; }
  .price { left: 74px; top: 566px; font-weight: 800; font-style: italic; color: var(--teal); font-size: 88px; line-height: 1; letter-spacing: -3px; }
  .price sup { font-size: 44px; vertical-align: 28px; }
  .per-area { left: 258px; top: 589px; width: 173px; height: 52px; background: var(--teal); border-radius: 6px 6px 6px 0;
    color: var(--ink); font-weight: 700; font-style: italic; font-size: 30px; text-align: center; line-height: 52px; }
  .fsa { left: 57px; width: 398px; top: 680px; text-align: center; font-size: 28px; font-weight: 500; color: var(--light-text); }
  .award { left: 66px; top: 741px; width: 100px; height: 100px; border-radius: 50%; background: var(--white); border: 6px solid #c8317a; }
  .award-note { left: 216px; top: 763px; font-size: 21px; color: var(--grey-text); line-height: 1.35; }
  .hero-photo { left: 553px; top: 0; width: 377px; height: 401px; }
  .panel { left: 0; top: 0; width: 973px; height: 900px; }
  .treating-tab { left: 531px; top: 629px; width: 229px; height: 40px; background: var(--orange);
    clip-path: polygon(0 0, 88% 0, 100% 100%, 0 100%); font-weight: 700; font-size: 30px; line-height: 40px; padding-left: 24px; }
  .conditions { left: 566px; top: 680px; list-style: none; font-size: 27px; font-weight: 500; color: var(--ink); line-height: 1.25; }
  .conditions li { display: flex; gap: 12px; margin-bottom: 10px; }
  .conditions svg { flex: none; margin-top: 6px; }
  .services { left: 0; width: 973px; text-align: center; font-weight: 700; font-size: 38px; line-height: 1.2; letter-spacing: .5px; }
  .services .sep { display: inline-block; width: 20px; height: 20px; border-radius: 50%; border: 3px solid var(--orange);
    background: radial-gradient(var(--orange) 45%, transparent 50%); margin: 0 18px; vertical-align: 4px; }
  .disclaimer { left: 0; width: 973px; top: 978px; text-align: center; font-size: 18px; color: var(--grey-text); }
  .footer-paper { left: 0; top: 1024px; width: 973px; height: 176px; }
  .office { top: 1098px; font-size: 14px; color: var(--dark-text); line-height: 1.4; }
  .office h3 { display: flex; align-items: center; gap: 6px; font-size: 17px; font-weight: 700; color: var(--teal); margin-left: -22px; }
  .contact { left: 694px; top: 1096px; color: var(--dark-text); }
  .contact .label { font-size: 16px; font-weight: 600; }
  .contact .phone { display: flex; align-items: center; gap: 6px; font-size: 25px; font-weight: 700; line-height: 1.2; }
  .contact .web { font-size: 21px; font-weight: 700; }
  .contact .web span { color: var(--orange); }
</style>
</head>
<body>
<main class="flyer">
  <svg class="abs panel" viewBox="0 0 973 900" aria-hidden="true">
    <path d="M510 265 C520 340 540 390 560 417 L530 417 L530 830 Q530 849 550 849 L917 849 L917 570 L927 565 L973 565 L973 570 L917 570 L917 417 L560 417 Z" fill="var(--teal)"/>
    <path d="M510 265 C520 340 560 400 600 430 L530 430 Z" fill="var(--teal)"/>
  </svg>
  <div class="abs hero-photo" role="img" aria-label="Photo of a person holding a sore ankle, greyscale with orange glow at the pain point"
       style="background: radial-gradient(circle at 45% 45%, rgba(240,122,62,.7) 0 12%, transparent 30%), linear-gradient(160deg, #cfcfcf 0%, #8e8e8e 45%, #444 80%, var(--ink) 100%); clip-path: polygon(8% 0, 100% 0, 100% 70%, 70% 100%, 30% 100%, 25% 60%, 10% 25%);"></div>
  <svg class="abs" style="left:540px;top:402px" width="400" height="230" aria-hidden="true">
    <circle cx="99" cy="99" r="92" fill="#2a2a2a"/>
    <circle cx="287" cy="119" r="110" fill="#2a2a2a"/>
  </svg>
  <div class="abs" role="img" aria-label="Photo of a PRP injection into a heel" style="left:553px;top:415px;width:172px;height:172px;border-radius:50%;background:radial-gradient(circle at 55% 60%, #f28b4a 0 14%, #e9b08f 30%, #f4f4f4 70%);"></div>
  <div class="abs" role="img" aria-label="Photo of gloved hands loading blood tubes into a centrifuge" style="left:731px;top:425px;width:212px;height:212px;border-radius:50%;background:radial-gradient(circle at 40% 65%, #2d3f6a 0 22%, #cfcfcf 45%, #efe6dc 80%);"></div>

  <div class="abs brand"><span class="brand-dot"></span><span class="brand-name">MEADOWBROOK<br>FOOT &amp; ANKLE</span></div>

  <div class="abs script">Platelet Rich</div>
  <h1 class="abs headline plasma">PLASMA</h1>
  <div class="abs headline therapy">THERAPY</div>
  <div class="abs abbr">(PRP)</div>

  <div class="abs price-tab">Self pay price:</div>
  <div class="abs price-box"></div>
  <div class="abs price"><sup>$</sup>199</div>
  <div class="abs per-area">PER AREA</div>
  <div class="abs fsa">FSA/HSA Eligible.</div>

  <div class="abs award" role="img" aria-label="Award badge"></div>
  <p class="abs award-note">Text Content Needed<br>for this Section.</p>

  <div class="abs treating-tab">TREATING</div>
  <ul class="abs conditions">
    <li><svg width="26" height="26" viewBox="0 0 26 26"><circle cx="13" cy="13" r="10.5" fill="none" stroke="var(--ink)" stroke-width="3"/><path d="M8 13l4 4 10-11" fill="none" stroke="var(--ink)" stroke-width="3" stroke-linecap="round"/></svg>Plantar Fasciitis</li>
    <li><svg width="26" height="26" viewBox="0 0 26 26"><circle cx="13" cy="13" r="10.5" fill="none" stroke="var(--ink)" stroke-width="3"/><path d="M8 13l4 4 10-11" fill="none" stroke="var(--ink)" stroke-width="3" stroke-linecap="round"/></svg>Achilles Tendonitis</li>
    <li><svg width="26" height="26" viewBox="0 0 26 26"><circle cx="13" cy="13" r="10.5" fill="none" stroke="var(--ink)" stroke-width="3"/><path d="M8 13l4 4 10-11" fill="none" stroke="var(--ink)" stroke-width="3" stroke-linecap="round"/></svg>Tendon &amp; Ligament<br>Injuries</li>
  </ul>

  <div class="abs services" style="top:880px">PODIATRY<span class="sep"></span>FOOT &amp; ANKLE SURGERY</div>
  <div class="abs services" style="top:926px">SPORTS MEDICINE<span class="sep"></span>WOUND CARE</div>
  <p class="abs disclaimer">*A consultation is necessary to determine your eligibility.</p>

  <svg class="abs footer-paper" viewBox="0 0 973 176" preserveAspectRatio="none" aria-hidden="true">
    <path d="M0 12 L40 6 L90 10 L150 4 L210 11 L280 5 L350 9 L420 3 L500 10 L570 5 L640 11 L720 4 L800 9 L880 5 L973 10 L973 176 L0 176 Z" fill="#dcdcdc"/>
    <path d="M0 22 L60 18 L130 24 L200 17 L270 23 L340 19 L420 25 L500 18 L580 24 L660 19 L740 24 L820 18 L900 23 L973 20 L973 176 L0 176 Z" fill="var(--paper)"/>
  </svg>

  <div class="abs office" style="left:58px">
    <h3><svg width="16" height="16" viewBox="0 0 16 16"><circle cx="8" cy="8" r="7.5" fill="var(--orange)"/><circle cx="8" cy="7" r="2.5" fill="#fff"/></svg>Millbrook Office</h3>
    58 Harbor View Dr.<br>Suite 120<br>Millbrook, MD 21000
  </div>
  <div class="abs office" style="left:281px">
    <h3><svg width="16" height="16" viewBox="0 0 16 16"><circle cx="8" cy="8" r="7.5" fill="var(--orange)"/><circle cx="8" cy="7" r="2.5" fill="#fff"/></svg>Riverton Office</h3>
    77 Wellness Way<br>Riverton, WV 25000
  </div>
  <div class="abs office" style="left:492px">
    <h3><svg width="16" height="16" viewBox="0 0 16 16"><circle cx="8" cy="8" r="7.5" fill="var(--orange)"/><circle cx="8" cy="7" r="2.5" fill="#fff"/></svg>Oakdale Office</h3>
    2210 Linden Ave.<br>Ste. 305<br>Oakdale, MD 21099
  </div>
  <div class="abs contact">
    <div class="label">CONTACT US TODAY</div>
    <div class="phone"><svg width="20" height="20" viewBox="0 0 20 20"><circle cx="10" cy="10" r="9.5" fill="var(--orange)"/><path d="M7 5l2 3-1.2 1.2a7 7 0 003 3L12 11l3 2-1 2c-4 0-9-5-9-9z" fill="#fff"/></svg>(555) 214-0390</div>
    <div class="web">www.<span>stepwellclinic</span>.com</div>
  </div>
</main>
</body>
</html>
```